Web Site Design for a Finance (lending) Company

We are opening a new subsidiary that focuses on lending money in the real estate industry. We need a web site designed to represent the business.

The business is lending money to real estate investors. A typical client/borrower will be looking to borrow money to buy a house, renovate it and then sell it at a profit, all within 12 months or less.

Company name is Brevand Finance. Our logo is attached.

Attached is a general outline for the web site. We're working on writing more text for each page but this should give you enough to get started with some ideas.

Competitor web site that I like a lot (as an example): https://quorvelfunding.com/. Many of the general items on this site match what we will need (description of loan programs, FAQ)

Target Market(s)

Real estate investors (generally individuals or small companies with just a few people) who are buying homes, renovating them and then selling them at a profit.

Industry/Entity Type

Finance

Coding

Coded - Design and coding required

Number of Pages Required

5+ page

Colors

Designer to choose colors to be used in the design.

Requirements
Must have
• Minimalist design. Clean lines without too much clutter. Some stock photography is ok but the photos should not be distracting. They should almost fade in to the background so that user can focus on the key information about what our company does instead. We are a finance company, not a design company, so the information about our products will be more interesting to site visitors than the art.
• Some minimalist examples from Snapboard:
• https://www.snapboard-example.com/explore/minimalist-web-design/
Nice to have
• If you search in seekly for "hard money lenders" you will find many examples of web sites from our competition. I have provided a link above to competitor web site that I like a lot.
• I have attached our logo in EPS format. Logo is green. Web site doesn't have to be green but it should be of a color that will work well with the logo.

```html
<!DOCTYPE html>
<html lang="en">
<head>
<meta charset="utf-8">
<title>Brevand Finance — Loans &amp; Contact</title>
<link href="https://fonts.googleapis.com/css2?family=Questrial&display=swap" rel="stylesheet">
<style>
  :root{
    --brown:#7b5a43;
    --brown-deep:#5f4331;
    --green:#2f5b3e;
    --green-deep:#1f4029;
    --ink:#111111;
    --white:#ffffff;
    --gold:#a8792f;
    --charcoal:#26282a;
    --charcoal-soft:#323840;
    --wood:#4c3a2d;
    --wood-deep:#2e241d;
    --rule:#d9d9d9;
  }
  *{box-sizing:border-box;margin:0;padding:0}
  html,body{width:1040px;height:1200px;overflow:hidden;background:var(--white)}
  body{position:relative;font-family:"Questrial",sans-serif;color:var(--white)}

  .loans{position:absolute;left:0;top:0;width:1040px;height:374px;display:flex;box-shadow:0 3px 6px rgba(0,0,0,.25);z-index:2}
  .loan{position:relative;width:520px;height:374px;text-align:center}
  .loan__photo{position:absolute;inset:0}
  .loan--flip .loan__photo{background:linear-gradient(160deg,#8a6a52 0%,var(--brown) 45%,var(--brown-deep) 100%)}
  .loan--commercial .loan__photo{background:linear-gradient(200deg,var(--green-deep) 0%,var(--green) 50%,#3a6a48 100%)}
  .loan__title{position:absolute;left:0;right:0;font-size:29px;font-weight:400;letter-spacing:2px;line-height:38px;text-shadow:0 2px 4px rgba(0,0,0,.35)}
  .loan--flip .loan__title{top:53px}
  .loan--commercial .loan__title{top:34px}
  .loan__text{position:absolute;left:60px;right:60px;font-size:16.5px;line-height:24.8px;letter-spacing:1.2px;text-transform:uppercase}
  .loan--flip .loan__text{top:133px}
  .loan--commercial .loan__text{top:131px}
  .btn{position:absolute;display:block;border:1px solid var(--white);border-radius:18px;color:var(--white);text-decoration:none;text-align:center;letter-spacing:2px;box-shadow:0 2px 4px rgba(0,0,0,.3)}
  .loan .btn{left:332px;top:318px;width:125px;height:32px;line-height:30px;font-size:12.5px}

  .contact-head{position:absolute;left:0;top:460px;width:1040px;text-align:center}
  .contact-head__title{font-size:36px;font-weight:400;letter-spacing:8px;color:var(--ink);line-height:46px}
  .divider{position:absolute;left:450px;top:510px}

  .contact{position:absolute;left:0;top:621px;width:1040px;height:579px}
  .contact__aside{position:absolute;left:0;top:0;width:409px;height:579px;background:linear-gradient(180deg,var(--charcoal-soft) 0%,var(--charcoal) 40%,#1f2123 100%)}
  .contact__photo{position:absolute;left:409px;top:0;width:631px;height:579px;background:linear-gradient(135deg,var(--wood) 0%,#5a4535 45%,var(--wood-deep) 100%)}

  .touch{position:absolute;left:52px;top:150px;font-size:38px;letter-spacing:7px;line-height:48px;font-weight:400}
  .touch__accent{display:block;color:var(--gold)}
  .info{position:absolute;left:56px;list-style:none;font-size:12.5px;letter-spacing:1.8px}
  .info li{display:flex;align-items:center;height:33px}
  .info svg{width:16px;margin-right:18px}
  .info{top:269px}

  .brand{position:absolute;left:60px;top:1006px;display:flex;align-items:center;gap:14px;color:#5e7f8c;font-size:30px;line-height:34px}
  .brand__mark{width:40px;height:40px;border:2px solid #5e7f8c}

  .social{position:absolute;left:128px;top:1163px;display:flex;gap:26px}
  .social span{width:22px;height:22px;border:1.5px solid var(--gold);border-radius:50%}

  .form{position:absolute;left:527px;top:762px;width:383px}
  .field{display:block;height:53px;border-bottom:1px solid var(--rule);position:relative}
  .field span{position:absolute;left:11px;bottom:8px;font-size:12.5px;letter-spacing:1.6px}
  .btn--submit{left:863px;top:1082px;width:126px;height:32px;line-height:30px;font-size:16px;letter-spacing:3px;box-shadow:none;background:none}
  .legal{position:absolute;left:550px;top:1176px;font-size:8.5px;letter-spacing:.6px}
</style>
</head>
<body>
  <section class="loans">
    <article class="loan loan--flip">
      <div class="loan__photo" role="img" aria-label="Warm brown-toned landscape photo of hills and a winding road"></div>
      <h2 class="loan__title">FIX AND FLIP LOANS</h2>
      <p class="loan__text">Lorem ipsum dolor sit amet, consectetur adipiscing elit. Aliquam quis varius ante. Etiam ornare, justo a cursus hendrerit, ex sapien consectetur eros, non dictum ex ex vel quam. Nam metus justo</p>
      <a class="btn" href="#">READ MORE</a>
    </article>
    <article class="loan loan--commercial">
      <div class="loan__photo" role="img" aria-label="Green-toned photo of a tree-lined street with a parked bicycle"></div>
      <h2 class="loan__title">COMMERCIAL HARD<br>MONEY LOANS</h2>
      <p class="loan__text">Lorem ipsum dolor sit amet, consectetur adipiscing elit. Aliquam quis varius ante. Etiam ornare, justo a cursus hendrerit, ex sapien consectetur eros, non dictum ex ex vel quam. Nam metus justo</p>
      <a class="btn" href="#">READ MORE</a>
    </article>
  </section>

  <header class="contact-head">
    <h2 class="contact-head__title">CONTACT US</h2>
  </header>
  <svg class="divider" width="140" height="24" viewBox="0 0 140 24">
    <line x1="0" y1="12" x2="55" y2="12" stroke="#111" stroke-width="1"/>
    <line x1="86" y1="12" x2="140" y2="12" stroke="#111" stroke-width="1"/>
    <polyline points="63,5 70,12 63,19" fill="none" stroke="#a8792f" stroke-width="1.6"/>
    <polyline points="69,5 76,12 69,19" fill="none" stroke="#a8792f" stroke-width="1.6"/>
  </svg>

  <section class="contact">
    <div class="contact__aside" role="img" aria-label="Dark, muted photo of a brick building on a city street at dusk">
      <h2 class="touch">GET IN<span class="touch__accent">TOUCH</span></h2>
      <ul class="info">
        <li><svg viewBox="0 0 16 12"><rect x=".5" y=".5" width="15" height="11" fill="none" stroke="#fff"/><polyline points=".5,.5 8,7 15.5,.5" fill="none" stroke="#fff"/><line x1=".5" y1="11.5" x2="6" y2="5.5" stroke="#fff"/><line x1="15.5" y1="11.5" x2="10" y2="5.5" stroke="#fff"/></svg>INFO@BREVANDFINANCE.COM</li>
        <li><svg viewBox="0 0 16 16"><path d="M3 1l3 3-1.5 2c1 2 3 4 5 5l2-1.5 3 3-2 2C7 14 2 9 1 3z" fill="#fff"/></svg>0198-765-432</li>
      </ul>
    </div>
    <div class="contact__photo" role="img" aria-label="Top-down photo of a wooden meeting table with business people shaking hands"></div>
  </section>

  <div class="brand"><span class="brand__mark"></span>Brevand Finance</div>
  <nav class="social" aria-label="Social links"><span></span><span></span><span></span><span></span></nav>

  <form class="form">
    <label class="field"><span>First name</span></label>
    <label class="field"><span>Last name</span></label>
    <label class="field"><span>Email</span></label>
    <label class="field"><span>How you heard about us</span></label>
  </form>
  <a class="btn btn--submit" href="#">SUBMIT</a>
  <p class="legal">© 2017 BREVAND FINANCE - ALL INTELLECTUAL PROPERTY RIGHTS RESEVED</p>
</body>
</html>
```